BKA

Please send us some options for letterhead I attached our Logo. In addition to the Logo we need this information somewhere on the page

47 Fenbury Lane
Brenford, CT 06817
203-481-7629

```html
<!DOCTYPE html>
<html lang="en">
<head>
<meta charset="utf-8">
<title>BKA Letterhead</title>
<link rel="stylesheet" href="https://fonts.googleapis.com/css2?family=Arimo:wght@400;700&display=swap">
<style>
  :root {
    --paper: #ffffff;
    --blue-deep: #0a7bc7;
    --blue-mid: #2a9bd6;
    --blue-light: #6fcbe6;
    --brand-dark: #4a3f3b;
    --text-light: #ffffff;
  }
  * { margin: 0; padding: 0; box-sizing: border-box; }
  html, body {
    width: 981px;
    height: 1200px;
    overflow: hidden;
    background: var(--paper);
  }
  .letterhead {
    position: relative;
    width: 981px;
    height: 1200px;
    background: var(--paper);
    font-family: "Arimo", Arial, sans-serif;
  }
  .header-band {
    position: absolute;
    top: 0;
    left: 0;
    width: 981px;
    height: 216px;
  }
  .brand {
    position: absolute;
    top: 40px;
    left: 50px;
    display: flex;
    align-items: center;
    gap: 20px;
  }
  .brand-mark {
    width: 100px;
    height: 100px;
    background: var(--brand-dark);
  }
  .brand-name {
    font-size: 80px;
    font-weight: 700;
    letter-spacing: 3px;
    color: var(--text-light);
    line-height: 1;
  }
  .contact {
    position: absolute;
    top: 50px;
    left: 704px;
    color: var(--text-light);
    font-size: 18px;
    font-weight: 700;
    font-style: normal;
    line-height: 1.3;
  }
  .contact-phone {
    display: flex;
    align-items: center;
    gap: 7px;
    margin-bottom: 12px;
  }
  .contact-phone svg { width: 16px; height: 16px; }
</style>
</head>
<body>
  <main class="letterhead">
    <svg class="header-band" viewBox="0 0 981 216" aria-hidden="true">
      <defs>
        <radialGradient id="band-glow" cx="540" cy="70" r="470" gradientUnits="userSpaceOnUse">
          <stop offset="0" stop-color="var(--blue-light)"/>
          <stop offset="0.55" stop-color="var(--blue-mid)"/>
          <stop offset="1" stop-color="var(--blue-deep)"/>
        </radialGradient>
      </defs>
      <path d="M0,0 H981 V42 C940,150 760,190 520,190 C330,190 80,170 0,214 Z" fill="url(#band-glow)"/>
    </svg>

    <div class="brand">
      <span class="brand-mark"></span>
      <span class="brand-name">BKA</span>
    </div>

    <address class="contact">
      <div class="contact-phone">
        <svg viewBox="0 0 24 24" aria-hidden="true">
          <path d="M6.6 10.8a15.1 15.1 0 0 0 6.6 6.6l2.2-2.2a1 1 0 0 1 1-.25 11.4 11.4 0 0 0 3.6.57 1 1 0 0 1 1 1V20a1 1 0 0 1-1 1A17 17 0 0 1 3 4a1 1 0 0 1 1-1h3.5a1 1 0 0 1 1 1c0 1.25.2 2.45.57 3.6a1 1 0 0 1-.25 1z" fill="none" stroke="currentColor" stroke-width="2"/>
        </svg>
        <span>203-481-7629</span>
      </div>
      <div>47 Fenbury Lane</div>
      <div>Brenford, CT 06817</div>
    </address>
  </main>
</body>
</html>
```